Simple and Clean business card design

We would like the design to be simple clean and to incorporate our colors.

We are open to your design and talent, we have the dots in our logo as we think of it as data points and we connect data points for people.

We are open to see the great creative and clean design you bring to the table

Contact Information for Business Card

please include: name, position, email, phone and website

Font styles to use
Sans Serif

Requirements
Must have
• my colors incorporated, simplicity
Nice to have
• lots of white space, simplicity
Should not have
• complexicity/ complex art

```html
<!DOCTYPE html>
<html lang="en">
<head>
<meta charset="utf-8">
<title>Lumora Business Card</title>
<link href="https://fonts.googleapis.com/css2?family=Montserrat:wght@300;400;700&family=Open+Sans:wght@400;600&display=swap" rel="stylesheet">
<style>
  :root {
    --stage: #2b2b2b;
    --ink: #000000;
    --paper: #f1f1f1;
    --red: #d9392b;
    --yellow: #e8b00f;
    --green: #2e9e48;
    --blue: #4a72c4;
    --text-dark: #222222;
    --text-light: #f4f4f4;
    --text-muted: #cfcfcf;
  }
  * { margin: 0; padding: 0; box-sizing: border-box; }
  html, body {
    width: 1200px; height: 900px; overflow: hidden;
    background: var(--stage);
  }
  .stage { position: relative; width: 1200px; height: 900px; }
  .card {
    position: absolute; left: 330px; width: 540px; height: 310px;
    overflow: hidden; box-shadow: 0 10px 30px rgba(0,0,0,.45);
    display: flex;
  }
  .card--front { top: 120px; }
  .card--back { top: 480px; }
  .panel { position: relative; height: 100%; }
  .panel--ink { background: var(--ink); }
  .panel--paper { background: var(--paper); }
  .card--front .panel--ink { width: 230px; }
  .card--front .wave-art {
    width: 70px;
    background: linear-gradient(90deg, var(--ink) 0%, var(--red) 30%, var(--yellow) 55%, var(--green) 78%, var(--paper) 100%);
  }
  .card--front .panel--paper { flex: 1; }
  .card--back .panel--paper { width: 270px; }
  .card--back .wave-art {
    width: 60px;
    background: linear-gradient(90deg, var(--paper) 0%, var(--green) 25%, var(--yellow) 50%, var(--red) 72%, var(--ink) 100%);
  }
  .card--back .panel--ink { flex: 1; }
  .wave-art { height: 100%; flex: none; }
  .brand-name {
    position: absolute;
    font-family: "Open Sans", sans-serif; font-weight: 600;
    color: var(--ink); letter-spacing: 1px; line-height: 1;
    display: flex; align-items: center; gap: 10px; white-space: nowrap;
  }
  .brand-name__dot {
    width: 14px; height: 14px; border-radius: 50%; background: var(--blue);
  }
  .card--front .brand-name { left: 30px; top: 110px; font-size: 40px; }
  .card--back .brand-name { left: 36px; top: 46px; font-size: 40px; }
  .front-web {
    position: absolute; left: 40px; bottom: 38px;
    display: flex; align-items: center; gap: 12px; white-space: nowrap;
    font-family: "Montserrat", sans-serif; font-weight: 300; font-size: 12px;
    color: var(--text-light); letter-spacing: .5px;
  }
  .front-web__rule { width: 60px; height: 2px; background: var(--red); }
  .contact-list {
    position: absolute; left: 40px; top: 138px; list-style: none;
    font-family: "Open Sans", sans-serif; font-size: 13px; color: var(--text-dark);
  }
  .contact-list li { display: flex; align-items: flex-start; gap: 12px; margin-bottom: 9px; line-height: 1.3; white-space: nowrap; }
  .contact-icon {
    flex: none; width: 22px; height: 22px; border-radius: 50%;
    background: var(--blue); display: flex; align-items: center; justify-content: center;
  }
  .contact-icon svg { width: 12px; height: 12px; }
  .holder { position: absolute; left: 22px; top: 118px; white-space: nowrap; }
  .holder__name {
    font-family: "Montserrat", sans-serif; font-weight: 700; font-size: 21px;
    color: var(--text-light); letter-spacing: .3px;
  }
  .holder__role {
    font-family: "Montserrat", sans-serif; font-weight: 400; font-size: 10px;
    color: var(--text-muted); letter-spacing: 3.5px; margin-top: 6px;
  }
</style>
</head>
<body>
<main class="stage">

  <section class="card card--front" aria-label="Card front">
    <div class="panel panel--ink">
      <div class="front-web"><span class="front-web__rule"></span>www.lumora.com</div>
    </div>
    <div class="wave-art" role="img" aria-label="Decorative red, yellow and green curved bands"></div>
    <div class="panel panel--paper">
      <div class="brand-name">Lumora<span class="brand-name__dot"></span></div>
    </div>
  </section>

  <section class="card card--back" aria-label="Card back">
    <div class="panel panel--paper">
      <div class="brand-name">Lumora<span class="brand-name__dot"></span></div>
      <ul class="contact-list">
        <li>
          <span class="contact-icon"><svg viewBox="0 0 16 16"><path d="M4 1.5 6 5 4.6 6.4a8 8 0 0 0 5 5L11 10l3.5 2-1 2.5C8 15 1 8 1.5 2.5Z" fill="#fff"/></svg></span>
          <span>555-014-2087</span>
        </li>
        <li>
          <span class="contact-icon"><svg viewBox="0 0 16 16"><rect x="1.5" y="3.5" width="13" height="9" fill="none" stroke="#fff" stroke-width="1.4"/><path d="M1.5 3.5 8 9l6.5-5.5" fill="none" stroke="#fff" stroke-width="1.4"/></svg></span>
          <span>hello@lumora.com</span>
        </li>
        <li>
          <span class="contact-icon"><svg viewBox="0 0 16 16"><circle cx="8" cy="8" r="6.3" fill="none" stroke="#fff" stroke-width="1.3"/><ellipse cx="8" cy="8" rx="2.8" ry="6.3" fill="none" stroke="#fff" stroke-width="1.1"/><path d="M1.7 8h12.6" stroke="#fff" stroke-width="1.1"/></svg></span>
          <span>www.lumora.com</span>
        </li>
        <li>
          <span class="contact-icon"><svg viewBox="0 0 16 16"><path d="M8 15S3 9.5 3 6a5 5 0 0 1 10 0c0 3.5-5 9-5 9Z" fill="#fff"/><circle cx="8" cy="6" r="1.8" fill="var(--blue)"/></svg></span>
          <span>48 Linden Avenue<br>Austin, TX 5678</span>
        </li>
      </ul>
    </div>
    <div class="wave-art" role="img" aria-label="Decorative green, yellow and red curved bands"></div>
    <div class="panel panel--ink">
      <div class="holder">
        <div class="holder__name">MARCUS REED</div>
        <div class="holder__role">DESIGN SOLUTION</div>
      </div>
    </div>
  </section>

</main>
</body>
</html>
```